Orvane Business Hub Website Redesign

Objective: The primary goal of the website redesign is to effectively communicate with Small Business Owners, offering them custom business advisory services to drive growth. The redesigned website should be interactive, easy to read, and feature clear calls to action.

OBH provides custom business advisory services tailored to small enterprises, focusing on driving growth through a comprehensive 3-step process; Diagnostic, Remedial and Strategic roadmap development

1. Diagnostic Assessment:
a. In-depth analysis to identify business strengths, weaknesses, and opportunities.
b. Comprehensive evaluation to understand the unique needs of each small enterprise.
2. Remedial Care:
a. Implementation of tailored solutions to address identified issues.
b. Hands-on support to navigate challenges and obstacles.
3. Roadmap to Growth:
a. Development of a strategic roadmap outlining actionable steps for sustainable growth.
b. Ongoing guidance and support to ensure successful execution.

The Unique Selling Proposition (USP): OBH stands out by:
• Handholding businesses through their growth journey.
• Providing a clear roadmap to sustainable growth.
• Leveraging a network of industry experts for specialized advice.
Target Customers: OBH caters to the following target customers:
• Start-ups seeking to launch successfully.
• Businesses looking to achieve substantial growth.
• Entrepreneurial enterprises seeking support.
• Mature businesses facing distress and seeking turnaround strategies.
Services Offered:
1. Bespoke Packages:
a. Tailored advisory services to meet the unique needs of each client.
b. Personalized solutions for businesses at different stages of growth.
2. Training, Mentorship, and Coaching:
a. Skill-building programs for business owners and key staff.
b. Ongoing mentorship and coaching to foster continuous improvement.
3. Incubation:
a. Support for start-ups with physical and virtual resources.
b. Incubation programs to nurture and guide emerging businesses.
4. Specialized Programs:
a. Women Entrepreneurs:
b. Tailored programs to support and empower women in business.
c. Youth Entrepreneurs: Initiatives to cultivate and guide young entrepreneurs.

Design Preferences:
• Layout flow to tell the brand story
• Interactive design elements
• Easy-to-read and understand content.
• Clear and prominent calls to action.
Key Messages:
• Expert Business Advisory for Small Enterprises.
• Your Partner in Growth – from Assessment to Execution.
• Join a Network of Successful Entrepreneurs.
Brand Guidelines:
• Use the existing brand colors and logo.
• Maintain a professional and approachable tone throughout the website.
Deliverables:
• Responsive website design for desktop and mobile.
• Mockups for key pages.
• Clear navigation structure for easy user experience.
• Integration of interactive elements.

Similar Businesses
https://trellowventures.co.uk/free-resources/
https://www.kestrinvale.ac.uk/business-services/engage-with-us/talent-and-insight/the-venture-desk/
https://www.foundermill.ng/the-venture-desk/
https://plumewardadvisory.io/

Design ad Layout Inspiration
https://volubrique.com/en/
https://www.qz-example.com/en_gl/big-data-analytics

Target Market(s)

OBH caters to the following target customers: • Start-ups seeking to launch successfully. • Businesses looking to achieve substantial growth. • Entrepreneurial enterprises seeking support. • Mature businesses facing distress and seeking turnaround strategies.

Industry/Entity Type

Business Consulting and Advisory

Number of Pages Required

3 page

Requirements
Must have
• • Clear and prominent calls to action.
Nice to have
• • Interactive design elements. • Easy-to-read and understand content.

```html
<!DOCTYPE html>
<html lang="en">
<head>
<meta charset="utf-8">
<title>Orvane Business Hub – Home and Investor Readiness</title>
<link href="https://fonts.googleapis.com/css2?family=Ubuntu:wght@500;700&family=Roboto:wght@400;500;700&display=swap" rel="stylesheet">
<style>
:root{
  --backdrop:#a0a1a3;
  --navy:#0f1f3d;
  --deep:#0b2a5b;
  --royal:#0b3d7e;
  --blue:#1f5fae;
  --title:#0d3b7a;
  --cyan:#36bfe0;
  --ink:#222831;
  --muted:#6b7280;
  --line:#e3e6ea;
  --mist:#f3f6fa;
  --white:#ffffff;
}
*{box-sizing:border-box;margin:0;padding:0}
html,body{width:693px;height:1200px;overflow:hidden;background:var(--backdrop)}
body{font-family:"Roboto",sans-serif;color:var(--ink)}
.board{position:absolute;left:0;top:0;width:1456px;height:2522px;background:var(--backdrop);transform:scale(0.47596);transform-origin:0 0}
.page{position:absolute;width:559px;background:var(--white);overflow:hidden;box-shadow:0 2px 6px rgba(0,0,0,.25)}
.page-home{left:151px;top:166px;height:1887px}
.page-readiness{left:746px;top:166px;height:2190px}
.abs{position:absolute}

/* header */
.site-header{position:absolute;left:0;top:0;width:559px;height:37px;background:var(--white);z-index:3}
.brand{position:absolute;left:67px;top:6px;display:flex;align-items:center;gap:4px}
.brand-dot{width:9px;height:9px;border-radius:50%;background:var(--cyan)}
.brand-name{font-family:"Ubuntu",sans-serif;font-weight:700;color:var(--title);font-size:10px;line-height:11px;width:60px}
.main-nav{position:absolute;top:17px;display:flex;gap:17px;font-size:5.6px;font-weight:500;color:var(--ink);text-transform:uppercase}
.login{position:absolute;left:446px;top:13px;width:46px;height:17px;border-radius:9px;background:var(--cyan);color:#fff;font-size:5.6px;font-weight:700;display:flex;align-items:center;justify-content:center}

/* hero */
.hero{position:absolute;left:0;top:37px;width:559px;overflow:hidden}
.hero-photo{position:absolute;inset:0;background:linear-gradient(100deg,#5f6c7c 0%,#9aa6b3 35%,#c7ced6 60%,#7c8896 100%)}
.hero svg{position:absolute;inset:0;width:100%;height:100%}
.hero-title{position:absolute;font-family:"Ubuntu",sans-serif;font-weight:700;color:#fff;font-size:26px;line-height:29px;text-transform:uppercase}
.hero-btn{position:absolute;height:17px;border-radius:9px;background:var(--cyan);color:#fff;font-size:5.6px;font-weight:700;display:flex;align-items:center;justify-content:center}
.hero-dots{position:absolute;width:3px;display:flex;flex-direction:column;gap:4px}
.hero-dots i{display:block;width:3px;height:3px;border-radius:50%;background:#fff}

/* section titles */
.section-title{position:absolute;left:0;width:559px;text-align:center;font-family:"Ubuntu",sans-serif;font-weight:700;color:var(--title);font-size:26px;line-height:28px;text-transform:uppercase}
.pulse{position:absolute;width:62px;height:12px}
.pulse path{fill:none;stroke:var(--cyan);stroke-width:1.2}

/* about */
.about-lead{position:absolute;left:130px;top:370px;width:300px;text-align:center;font-size:5.6px;line-height:9px;color:#444}
.step-card{position:absolute;top:414px;width:137px;height:148px;border:2px solid var(--deep);background:#fff}
.step-card::before{content:"";position:absolute;left:-2px;top:-2px;border-left:12px solid var(--blue);border-bottom:60px solid transparent}
.step-card::after{content:"";position:absolute;right:-2px;bottom:-2px;border-right:10px solid var(--blue);border-top:60px solid transparent}
.step-icon{position:absolute;left:16px;top:12px;width:34px;height:36px;border-radius:3px;background:linear-gradient(135deg,#dfe7f1,#b9c9de)}
.step-num{position:absolute;right:12px;top:12px;font-family:"Ubuntu",sans-serif;font-weight:700;color:var(--cyan);font-size:18px}
.step-name{position:absolute;left:16px;top:64px;font-size:7.6px;font-weight:500;color:var(--ink)}
.bullets{list-style:none;font-size:4.6px;line-height:8px;color:#555}
.bullets li{position:relative;padding-left:7px}
.bullets li::before{content:"";position:absolute;left:1px;top:3px;width:2.5px;height:2.5px;border-radius:50%;background:var(--cyan)}
.step-card .bullets{position:absolute;left:16px;top:80px;width:108px}

/* services */
.services-bg{position:absolute;left:0;top:595px;width:559px;height:423px;background:var(--mist)}
.services-bg svg{position:absolute;inset:0;width:100%;height:100%}
.service-card{position:absolute;width:208px;height:100px;border-radius:30px;background:#fff;box-shadow:0 3px 5px rgba(15,31,61,.16)}
.service-icon{position:absolute;left:7px;top:17px;width:66px;height:66px;border-radius:50%}
.service-icon.cyan{background:var(--cyan)}
.service-icon.navy{background:var(--royal)}
.service-name{position:absolute;left:82px;top:18px;font-size:7.6px;line-height:9px;font-weight:500}
.service-card .bullets{position:absolute;left:82px;width:116px}

/* investor tool */
.tool{position:absolute;left:0;top:1018px;width:559px;height:257px;background:var(--royal)}
.tool-title{position:absolute;left:66px;top:34px;font-family:"Ubuntu",sans-serif;font-weight:700;color:#fff;font-size:25px;line-height:30px}
.tool-text{position:absolute;left:67px;top:116px;width:225px;font-size:5.7px;line-height:9px;color:#e4ebf5}
.tool-btn{position:absolute;left:67px;top:193px;width:142px;height:17px;border-radius:9px;background:var(--cyan);color:#fff;font-size:5.3px;font-weight:700;display:flex;align-items:center;justify-content:center}
.tool-photo{position:absolute;left:317px;top:32px;width:173px;height:190px;background:linear-gradient(160deg,#d9dde2,#8e9aaa 60%,#2d4f86);clip-path:polygon(10% 0,100% 0,100% 100%,0 100%)}

/* posts */
.post-card{position:absolute;top:1378px;width:137px;height:194px;background:#fff;box-shadow:0 1px 4px rgba(0,0,0,.15)}
.post-photo{position:absolute;left:5px;top:4px;width:127px;height:99px;background:linear-gradient(135deg,#3f4c5e,#9aa4b0 55%,#d8dce1)}
.post-title{position:absolute;left:9px;top:114px;width:122px;font-size:7px;line-height:9px;font-weight:500}
.post-text{position:absolute;left:9px;top:142px;width:122px;font-size:4.6px;line-height:8px;color:#a0a4aa}
.post-meta{position:absolute;left:9px;top:176px;font-size:4.2px;color:#777;display:flex;gap:8px}
.view-more{position:absolute;left:247px;top:1591px;width:66px;height:17px;border-radius:9px;background:var(--cyan);color:#fff;font-size:5.6px;font-weight:700;display:flex;align-items:center;justify-content:center}

/* footer */
.site-footer{position:absolute;left:0;bottom:0;width:559px;height:265px}
.site-footer > svg{position:absolute;inset:0;width:100%;height:100%}
.footer-badge{position:absolute;left:66px;top:-12px;width:108px;height:90px;border-radius:0 0 54px 54px;background:#fff;display:flex;align-items:center;justify-content:center}
.footer-badge .brand{position:static}
.footer-col{position:absolute;top:79px;color:#fff}
.footer-col h4{font-size:6.4px;font-weight:500;text-transform:uppercase;margin-bottom:14px;position:relative}
.footer-col h4::after{content:"";position:absolute;left:0;bottom:-6px;width:16px;height:1.5px;background:var(--cyan)}
.footer-col ul{list-style:none;font-size:4.6px;line-height:12.4px;color:#d5dbe6}
.contact-item{display:flex;align-items:center;gap:8px;font-size:4.6px;line-height:7px;color:#d5dbe6;margin-bottom:9px;width:110px}
.contact-item svg{flex:none;width:18px;height:18px}
.newsletter{position:absolute;left:72px;top:198px;display:flex;align-items:center}
.newsletter span{font-size:6.3px;font-weight:500;color:#fff;width:96px}
.newsletter .field{width:190px;height:16px;background:#fff;font-size:4.4px;color:#999;padding-left:8px;display:flex;align-items:center}
.newsletter .send{width:25px;height:16px;background:var(--cyan);display:flex;align-items:center;justify-content:center}
.socials{position:absolute;left:398px;top:201px;display:flex;gap:7px}
.socials i{display:block;width:11px;height:11px;border-radius:50%;background:var(--blue)}
.copyright{position:absolute;left:0;width:559px;top:247px;text-align:center;font-size:4.6px;color:#fff}

/* questionnaire */
.quiz{position:absolute;left:72px;top:280px;width:414px}
.question{padding:12px 0 12px 35px;border-bottom:1px solid var(--line)}
.question p{font-size:7.2px;line-height:9px;color:var(--ink)}
.options{display:flex;flex-wrap:wrap;gap:0 10px;margin-top:9px;font-size:5.1px;line-height:8px;color:#444}
.options span{display:flex;align-items:center;gap:4px}
.options span::before{content:"";width:6px;height:6px;border:1px solid #9aa0a8;border-radius:50%}
</style>
</head>
<body>
<div class="board">

<!-- HOME PAGE -->
<section class="page page-home">
  <header class="site-header">
    <div class="brand"><span class="brand-dot"></span><span class="brand-name">Orvane Business Hub</span></div>
    <nav class="main-nav" style="left:170px"><span>Home</span><span>About OBH</span><span>Services</span><span>Contact Us</span><span>Investor Readiness</span></nav>
    <div class="login">LOGIN</div>
  </header>

  <div class="hero" style="height:233px">
    <div class="hero-photo" role="img" aria-label="Photo of two colleagues smiling while reviewing a tablet in an office"></div>
    <svg viewBox="0 0 559 233" preserveAspectRatio="none" aria-hidden="true">
      <polygon points="330,0 559,0 559,233 190,233" fill="#0f1f3d" opacity=".96"/>
      <polygon points="380,0 559,0 559,34" fill="#1f5fae"/>
      <polygon points="0,198 559,226 559,233 0,233" fill="#36bfe0"/>
    </svg>
    <div class="hero-title" style="left:180px;top:80px;width:200px;text-align:center">The Business Hub</div>
    <div class="hero-btn" style="left:246px;top:149px;width:66px">ABOUT US</div>
    <div class="hero-dots" style="left:520px;top:108px"><i></i><i></i><i></i></div>
  </div>

  <h2 class="section-title" style="top:318px">About OBH</h2>
  <svg class="pulse" style="left:248px;top:348px" viewBox="0 0 62 12" aria-hidden="true"><path d="M0 6H24L27 1L31 11L34 6H62"/></svg>
  <p class="about-lead">OBH provides custom business advisory services tailored to small enterprises, focusing on driving growth through a comprehensive three-step process:</p>

  <article class="step-card" style="left:67px">
    <div class="step-icon" role="img" aria-label="Checklist icon"></div><div class="step-num">01</div>
    <h3 class="step-name">Diagnostic Assessment</h3>
    <ul class="bullets"><li>In-depth analysis to identify business strengths, weaknesses, and opportunities.</li><li>Comprehensive evaluation to understand the unique needs of each small enterprise.</li></ul>
  </article>
  <article class="step-card" style="left:211px">
    <div class="step-icon" role="img" aria-label="Remedy kit icon"></div><div class="step-num">02</div>
    <h3 class="step-name">Remedial Care</h3>
    <ul class="bullets"><li>Implementation of tailored solutions to address identified issues.</li><li>Hands-on support to navigate challenges and obstacles.</li></ul>
  </article>
  <article class="step-card" style="left:355px">
    <div class="step-icon" role="img" aria-label="Growth roadmap icon"></div><div class="step-num">03</div>
    <h3 class="step-name">Roadmap to Growth</h3>
    <ul class="bullets"><li>In-depth analysis to identify business strengths, weaknesses, and opportunities.</li><li>Comprehensive evaluation to understand the unique needs of each small enterprise.</li></ul>
  </article>

  <div class="services-bg">
    <svg viewBox="0 0 559 423" preserveAspectRatio="none" aria-hidden="true">
      <polygon points="0,0 559,0 559,0 0,0" fill="#fff"/>
      <polygon points="0,0 559,0 300,25" fill="#fff"/>
      <polygon points="280,37 559,0 559,68" fill="#1457a0"/>
      <polygon points="0,360 559,400 559,423 0,423" fill="#36bfe0"/>
    </svg>
  </div>
  <h2 class="section-title" style="top:672px">Services Offered</h2>
  <svg class="pulse" style="left:248px;top:702px" viewBox="0 0 62 12" aria-hidden="true"><path d="M0 6H24L27 1L31 11L34 6H62"/></svg>

  <article class="service-card" style="left:67px;top:728px">
    <div class="service-icon cyan" role="img" aria-label="Diagnostic screen icon"></div>
    <h3 class="service-name">Diagnostic Assessment</h3>
    <ul class="bullets" style="top:34px"><li>In-depth analysis to identify business strengths, weaknesses, and opportunities.</li><li>Comprehensive evaluation to understand the unique needs of each small enterprise.</li></ul>
  </article>
  <article class="service-card" style="left:284px;top:728px">
    <div class="service-icon navy" role="img" aria-label="Training presentation icon"></div>
    <h3 class="service-name">Training, Mentorship,<br>and Coaching</h3>
    <ul class="bullets" style="top:42px"><li>Skill-building programs for business owners and key staff.</li><li>Ongoing mentorship and coaching to foster continuous improvement.</li></ul>
  </article>
  <article class="service-card" style="left:67px;top:840px">
    <div class="service-icon navy" role="img" aria-label="Incubation bulb icon"></div>
    <h3 class="service-name">Incubation</h3>
    <ul class="bullets" style="top:34px"><li>Support for start-ups with physical and virtual resources.</li><li>Incubation programs to nurture and guide emerging businesses.</li></ul>
  </article>
  <article class="service-card" style="left:284px;top:840px">
    <div class="service-icon cyan" role="img" aria-label="Entrepreneur programs icon"></div>
    <h3 class="service-name">Specialized Programs</h3>
    <ul class="bullets" style="top:34px"><li>Women Entrepreneurs:</li><li>Tailored programs to support and empower women in business.</li><li>Youth Entrepreneurs: Initiatives to cultivate and guide young entrepreneurs.</li></ul>
  </article>

  <section class="tool">
    <h2 class="tool-title">INVESTOR<br>READINESS TOOL</h2>
    <svg class="pulse" style="left:66px;top:96px" viewBox="0 0 62 12" aria-hidden="true"><path d="M0 6H10L13 1L17 11L20 6H62"/></svg>
    <p class="tool-text">Sed ut perspiciatis unde omnis iste natus error sit voluptatem accusantium doloremque laudantium, totam rem aperiam, eaque ipsa quae ab illo inventore veritatis et quasi architecto beatae vitae dicta sunt explicabo. Nemo enim ipsam voluptatem quia voluptas sit aspernatur aut odit aut fugit, sed quia consequuntur magni dolores eos qui ratione voluptatem sequi nesciunt. Neque porro quisquam est, qui dolorem ipsum quia dolor sit amet,</p>
    <div class="tool-btn">SUBSCRIBE TO OUR READINESS TOOL</div>
    <div class="tool-photo" role="img" aria-label="Photo of a smiling businesswoman working on a laptop"></div>
  </section>

  <h2 class="section-title" style="top:1318px">Latest Posts</h2>
  <svg class="pulse" style="left:248px;top:1348px" viewBox="0 0 62 12" aria-hidden="true"><path d="M0 6H24L27 1L31 11L34 6H62"/></svg>

  <article class="post-card" style="left:67px"><div class="post-photo" role="img" aria-label="Photo of a team meeting around a table"></div><h3 class="post-title">Sed ut perspiciatis unde omnis iste natus error sit ..</h3><p class="post-text">Lorem ipsum dolor sit amet, consectetur adipiscing elitsed do eiusmod tempor..</p><div class="post-meta"><span>By Admin</span><span>November 10 , 2017</span></div></article>
  <article class="post-card" style="left:210px"><div class="post-photo" role="img" aria-label="Photo of a businessman in a suit with arms crossed"></div><h3 class="post-title">Sed ut perspiciatis unde omnis iste natus error sit ..</h3><p class="post-text">Lorem ipsum dolor sit amet, consectetur adipiscing elitsed do eiusmod tempor..</p><div class="post-meta"><span>By Admin</span><span>November 10 , 2017</span></div></article>
  <article class="post-card" style="left:352px"><div class="post-photo" role="img" aria-label="Photo of colleagues working together at a laptop"></div><h3 class="post-title">Sed ut perspiciatis unde omnis iste natus error sit ..</h3><p class="post-text">Lorem ipsum dolor sit amet, consectetur adipiscing elitsed do eiusmod tempor..</p><div class="post-meta"><span>By Admin</span><span>November 10 , 2017</span></div></article>
  <div class="view-more">VIEW MORE</div>

  <footer class="site-footer">
    <svg viewBox="0 0 559 265" preserveAspectRatio="none" aria-hidden="true">
      <polygon points="0,42 559,12 559,265 0,265" fill="#0f1f3d"/>
      <polygon points="300,26 559,0 559,42 440,40" fill="#1457a0"/>
      <polygon points="0,222 400,236 0,240" fill="#36bfe0"/>
      <rect x="0" y="238" width="559" height="27" fill="#0f1f3d"/>
    </svg>
    <div class="footer-badge"><div class="brand"><span class="brand-dot"></span><span class="brand-name">Orvane Business Hub</span></div></div>
    <div class="footer-col" style="left:67px"><h4>Contact Us</h4>
      <div class="contact-item"><svg viewBox="0 0 18 18"><circle cx="9" cy="9" r="8.3" fill="none" stroke="#fff" stroke-width=".8"/><path d="M5.5 9.5L9 6.3L12.5 9.5V12.5H5.5Z" fill="#fff"/></svg>123,Sed ut perspiciatis unde omnis iste natus eptatem</div>
      <div class="contact-item"><svg viewBox="0 0 18 18"><circle cx="9" cy="9" r="8.3" fill="none" stroke="#fff" stroke-width=".8"/><path d="M6.3 5.5L8 5.2L8.6 7.2L7.6 8C8.1 9.2 8.9 10 10 10.5L10.8 9.5L12.8 10.1L12.5 11.8C9 12 6 9 6.3 5.5Z" fill="#fff"/></svg>Phone : +1 555 014 2290</div>
      <div class="contact-item"><svg viewBox="0 0 18 18"><circle cx="9" cy="9" r="8.3" fill="none" stroke="#fff" stroke-width=".8"/><rect x="5.5" y="6.5" width="7" height="5" fill="#fff"/><path d="M5.5 6.5L9 9.3L12.5 6.5" fill="none" stroke="#0f1f3d" stroke-width=".6"/></svg>Email : info@orvanehub.com</div>
    </div>
    <div class="footer-col" style="left:198px"><h4>Quick Links</h4><ul><li>Home</li><li>About us</li><li>Services</li><li>Process</li><li>Contact Us</li></ul></div>
    <div class="footer-col" style="left:297px"><h4>Other Links</h4><ul><li>Sitemap</li><li>Customer Support</li><li>Legal Notice</li><li>Terms and conditions</li><li>Privacy policy</li></ul></div>
    <div class="footer-col" style="left:404px"><h4>Services</h4><ul><li>Bespoke Packages</li><li>Training, Mentorship, and Coaching</li><li>Incubation</li><li>Specialized Programs</li></ul></div>
    <div class="newsletter"><span>SIGN UP NEWSLETTER</span><div class="field">Enter Email Address</div><div class="send"><svg width="9" height="9" viewBox="0 0 10 10"><path d="M1 5L9 1L7 9L5 6Z" fill="#fff"/></svg></div></div>
    <div class="socials" aria-label="Social links"><i></i><i></i><i></i><i></i><i></i></div>
    <p class="copyright">© copyright 2024 OBH.All Rights Reserved &nbsp;|&nbsp; Privacy policy</p>
  </footer>
</section>

<!-- INVESTOR READINESS PAGE -->
<section class="page page-readiness">
  <header class="site-header">
    <div class="brand"><span class="brand-dot"></span><span class="brand-name">Orvane Business Hub</span></div>
    <nav class="main-nav" style="left:171px"><span>Home</span><span>About OBH</span><span>Services</span><span>Contact Us</span><span>Investor Readiness</span></nav>
    <div class="login">LOGIN</div>
  </header>

  <div class="hero" style="height:148px">
    <div class="hero-photo" role="img" aria-label="Photo of two colleagues smiling while reviewing a tablet in an office"></div>
    <svg viewBox="0 0 559 148" preserveAspectRatio="none" aria-hidden="true">
      <polygon points="270,30 559,0 559,148 230,148" fill="#0f1f3d" opacity=".97"/>
      <polygon points="380,0 559,0 559,24" fill="#1f5fae"/>
      <polygon points="0,112 559,140 559,148 0,148" fill="#36bfe0"/>
    </svg>
    <div class="hero-title" style="left:315px;top:52px">Investor<br>Readiness</div>
    <div class="hero-dots" style="left:520px;top:106px"><i></i><i></i><i></i></div>
  </div>

  <h1 class="section-title" style="top:221px">Investor Readiness</h1>
  <svg class="pulse" style="left:248px;top:251px" viewBox="0 0 62 12" aria-hidden="true"><path d="M0 6H24L27 1L31 11L34 6H62"/></svg>

  <form class="quiz">
    <div class="question"><p>1.Does the Entrepreneur has any experience in running a business?</p><div class="options"><span>YES</span><span>NO</span></div></div>
    <div class="question"><p>2.If yes, for how many years</p><div class="options"><span>Less than a year</span><span>1 to 3 years</span><span>3 to 5years</span><span>5 to 7 years</span><span>Over 7 years</span></div></div>
    <div class="question"><p>3.Hass the entrepreneur been into any formal employment</p><div class="options"><span>YES</span><span>NO</span></div></div>
    <div class="question"><p>4.If yes, what is the highest position that you have held?</p><div class="options"><span>Senior management</span><span>Middle management</span><span>Supervisor</span><span>Others (specify)</span></div></div>
    <div class="question"><p>5.Is the business you want to start related to your experience?</p><div class="options"><span>YES</span><span>NO</span></div></div>
    <div class="question"><p>6.If yes, What is the level of relationship</p><div class="options"><span>Very Strongly related</span><span>Fairly related</span><span>Not related</span></div></div>
    <div class="question"><p>7.How is the business registered?</p><div class="options"><span>Sole Proprietor</span><span>Partnership</span><span>Limited Company</span><span>Others(specify)</span></div></div>
    <div class="question"><p>8.If it is not registered would you like to be guided on how to register your business?</p><div class="options"><span>YES</span><span>NO</span></div></div>
    <div class="question"><p>9.What problem is your business idea trying to resolve?</p><div class="options"><span>Unmet needs</span><span>Cost inefficiency</span><span>Inadequate needs</span><span>Others (specify)</span></div></div>
    <div class="question"><p>10.How big is the problem?</p><div class="options"><span>Very big</span><span>Relative</span><span>Do not know</span><span>Not sure</span></div></div>
    <div class="question"><p>11.Have you been able to validate the problem?</p><div class="options"><span>YES</span><span>NO</span></div></div>
    <div class="question"><p>12.How did you validate the problem?</p><div class="options"><span>Market Research</span><span>Product/Service is lacking in this location</span><span>Others (specify)</span></div></div>
    <div class="question"><p>13.Does the business has a compelling value proposition?</p><div class="options"><span>YES</span><span>NO</span></div></div>
    <div class="question"><p>14.If no, would you require the services of an expert to assist you with preparing one?</p><div class="options"><span>YES</span><span>NO</span></div></div>
    <div class="question"><p>15.What product/service do you intend to sell?</p></div>
    <div class="question"><p>16.Is the product ready to sell?</p><div class="options"><span>YES</span><span>NO</span></div></div>
    <div class="question"><p>17.If no, what is left/required to make the product/service ready for the market</p><div class="options"><span>Run out of cash</span><span>Waiting for raw materials</span><span>Need technical assistance</span><span>Others (specify)</span></div></div>
    <div class="question"><p>18.How do you intend to reach the market with your product/service?</p><div class="options"><span>Sell to wholesales</span><span>Sell to retailers</span><span>Sell directly to the end users</span><span>Others (specify)</span></div></div>
    <div class="question"><p>19.Who is your target group?</p><div class="options"><span>Mass market</span><span>Niche market</span><span>Special interest group</span><span>Others (specify)</span></div></div>
    <div class="question"><p>20.What differentiate your product from the others in the market?</p><div class="options"><span>Price</span><span>Size</span><span>Attributes</span><span>New never been developed</span></div></div>
    <div class="question"><p>21.How does the business intend to communicate to clients?</p><div class="options" style="gap:0 6px"><span>Social media</span><span>Word of mouth advertisement</span><span>Above the line advertisement</span><span>Below the line advertisement</span></div></div>
    <div class="question"><p>22.Does the business has a marketing plan?</p><div class="options"><span>YES</span><span>NO</span></div></div>
    <div class="question"><p>23.If no, would you want to be assisted to prepare one?</p><div class="options"><span>YES</span><span>NO</span></div></div>
    <div class="question"><p>24.Do you have a team with the necessary skills to assist you actualize your business idea?</p><div class="options"><span>YES</span><span>NO</span></div></div>
    <div class="question"><p>25.If no, would you like to be assisted to identify potential candidates that would meet your requirements</p></div>
    <div class="question"><p>26.Does the business require any financing?</p><div class="options"><span>YES</span><span>NO</span></div></div>
    <div class="question"><p>27.If so how much</p></div>
    <div class="question"><p>28.What type of financing do you require?</p><div class="options"><span>Equity Financing</span><span>Debt Financing</span><span>Lease</span></div></div>
    <div class="question"><p>29.Are you willing to give a stake in your business?</p></div>
    <div class="question"><p>30.If yes, what percentage?</p></div>
    <div class="question"><p>31.What is the percentage of the owner’s contribution to the business?</p></div>
    <div class="question"><p>32.Does the business have personnel that will assist the entrepreneur to actualize this business?</p><div class="options"><span>YES</span><span>NO</span></div></div>
    <div class="question"><p>33.Has the entrepreneur prepared a financial projections for the business?</p><div class="options"><span>YES</span><span>NO</span></div></div>
    <div class="question" style="border-bottom:0"><p>34.If No, would you like to be assisted to prepare one?</p><div class="options"><span>YES</span><span>NO</span></div></div>
  </form>

  <footer class="site-footer">
    <svg viewBox="0 0 559 265" preserveAspectRatio="none" aria-hidden="true">
      <rect x="0" y="0" width="559" height="265" fill="#fff"/>
      <polygon points="0,42 559,12 559,265 0,265" fill="#0f1f3d"/>
      <polygon points="300,26 559,0 559,42 440,40" fill="#1457a0"/>
      <polygon points="0,222 400,236 0,240" fill="#36bfe0"/>
      <rect x="0" y="238" width="559" height="27" fill="#0f1f3d"/>
    </svg>
    <div class="footer-badge"><div class="brand"><span class="brand-dot"></span><span class="brand-name">Orvane Business Hub</span></div></div>
    <div class="footer-col" style="left:67px"><h4>Contact Us</h4>
      <div class="contact-item"><svg viewBox="0 0 18 18"><circle cx="9" cy="9" r="8.3" fill="none" stroke="#fff" stroke-width=".8"/><path d="M5.5 9.5L9 6.3L12.5 9.5V12.5H5.5Z" fill="#fff"/></svg>123,Sed ut perspiciatis unde omnis iste natus eptatem</div>
      <div class="contact-item"><svg viewBox="0 0 18 18"><circle cx="9" cy="9" r="8.3" fill="none" stroke="#fff" stroke-width=".8"/><path d="M6.3 5.5L8 5.2L8.6 7.2L7.6 8C8.1 9.2 8.9 10 10 10.5L10.8 9.5L12.8 10.1L12.5 11.8C9 12 6 9 6.3 5.5Z" fill="#fff"/></svg>Phone : +1 555 014 2290</div>
      <div class="contact-item"><svg viewBox="0 0 18 18"><circle cx="9" cy="9" r="8.3" fill="none" stroke="#fff" stroke-width=".8"/><rect x="5.5" y="6.5" width="7" height="5" fill="#fff"/><path d="M5.5 6.5L9 9.3L12.5 6.5" fill="none" stroke="#0f1f3d" stroke-width=".6"/></svg>Email : info@orvanehub.com</div>
    </div>
    <div class="footer-col" style="left:198px"><h4>Quick Links</h4><ul><li>Home</li><li>About us</li><li>Services</li><li>Process</li><li>Contact Us</li></ul></div>
    <div class="footer-col" style="left:297px"><h4>Other Links</h4><ul><li>Sitemap</li><li>Customer Support</li><li>Legal Notice</li><li>Terms and conditions</li><li>Privacy policy</li></ul></div>
    <div class="footer-col" style="left:404px"><h4>Services</h4><ul><li>Bespoke Packages</li><li>Training, Mentorship, and Coaching</li><li>Incubation</li><li>Specialized Programs</li></ul></div>
    <div class="newsletter"><span>SIGN UP NEWSLETTER</span><div class="field">Enter Email Address</div><div class="send"><svg width="9" height="9" viewBox="0 0 10 10"><path d="M1 5L9 1L7 9L5 6Z" fill="#fff"/></svg></div></div>
    <div class="socials" aria-label="Social links"><i></i><i></i><i></i><i></i><i></i></div>
    <p class="copyright">© copyright 2024 OBH.All Rights Reserved &nbsp;|&nbsp; Privacy policy</p>
  </footer>
</section>

</div>
</body>
</html>
```